In need of an AWESOME website for our Water Re-filling Store

The project is to design a website for our retail store front with the website www.brookvalefillhouse.com. Currently if you go to that site it redirects you to our other site www.brookvalebottleworks.com which is just our water bottle website. So, I need a new website created for www.brookvalefillhouse.com (retail storefront)
Use our Squarespace to create a site with pages to help educate, tell about us, link to our water bottle brand site that is already created with Squarespace, and show the family and community aspects that we believe in. Our current water bottle website is www.brookvalebottleworks.com for reference
We also sell hydration products, especially QRVX products and have access to digital media through our QRVX dealer site. we sell bottles, dispensers and other supplies for water refilling customers. We sell Ice as well.

Target Market(s)

Local residents looking to fill up their 1-5 gallon water jugs

Industry/Entity Type

Alkaline and Purified Water Retail Re-filling Store

Coding

Coded - Design and coding required

Font styles to use
Serif
Sans Serif

Colors
0054AA
0677BA
7BADD7
CADEEF
E8F1F8

Requirements
Must have
• pictures of our family in the about us section and pictures of our store inside and out.

```html
<!DOCTYPE html>
<html lang="en">
<head>
<meta charset="utf-8">
<title>Brookvale Fill House</title>
<link href="https://fonts.googleapis.com/css2?family=Arimo:wght@400;500&family=Poppins:wght@400;500&display=swap" rel="stylesheet">
<style>
:root{
  --navy:#2b2a6c;
  --blue:#1d8fe1;
  --deep:#0054aa;
  --mid:#0677ba;
  --sky:#7badd7;
  --pale:#cadeef;
  --mist:#e8f1f8;
  --ink:#1c1c1c;
  --muted:#8a8a8a;
  --line:#e4e4e4;
  --soft:#f5f5f5;
  --white:#ffffff;
}
*{margin:0;padding:0;box-sizing:border-box}
html,body{width:1200px;height:4902px;overflow:hidden}
body{font-family:"Poppins",sans-serif;color:var(--ink);background:var(--white);position:relative}
.abs{position:absolute}
h1,h2,h3,.head{font-family:"Arimo",sans-serif;font-weight:400}
.btn{position:absolute;display:flex;align-items:center;justify-content:center;background:var(--blue);color:var(--white);border-radius:20px;font-size:12px;font-family:"Poppins",sans-serif}
.btn.ghost{background:transparent;border:1px solid var(--white)}
.photo{position:absolute}
/* top bar */
.topbar{top:0;left:0;width:1200px;height:30px;background:var(--navy);color:var(--white);font-size:12px;display:flex;align-items:center;justify-content:center}
/* hero */
.hero{top:30px;left:0;width:1200px;height:588px;background:linear-gradient(180deg,#5a5860 0%,#6d6a6c 30%,#8d9cc0 60%,#3d5f9e 100%)}
.hero-shade{top:30px;left:0;width:1200px;height:588px;background:linear-gradient(180deg,rgba(0,0,0,.25),rgba(10,20,60,.35))}
.brand{color:var(--white);font-family:"Arimo",sans-serif;font-size:13px;line-height:1.1;display:flex;align-items:center;gap:8px}
.brand .dot{width:22px;height:22px;border-radius:50%;border:2px solid var(--white)}
.nav{top:62px;left:352px;display:flex;gap:0;color:var(--white);font-size:12px}
.nav span{position:absolute;white-space:nowrap}
.hero h1{top:335px;left:0;width:1200px;text-align:center;color:var(--white);font-size:52px;line-height:54px}
.hero-sub{top:458px;left:0;width:1200px;text-align:center;color:var(--white);font-size:12px;line-height:19px}
/* section titles */
.title{position:absolute;left:0;width:1200px;text-align:center;font-size:33px;font-family:"Arimo",sans-serif}
/* service cards */
.card{position:absolute;border:1px solid var(--line);background:var(--white);text-align:center;box-shadow:0 1px 4px rgba(0,0,0,.05)}
.card svg{position:absolute;left:50%;transform:translateX(-50%)}
.card .name{position:absolute;left:0;width:100%;font-family:"Arimo",sans-serif;font-size:18px}
.card .desc{position:absolute;left:0;width:100%;font-size:11px;color:var(--muted);line-height:17px}
/* about */
.about-h{top:1034px;left:112px;font-size:32px;line-height:40px}
.about-p{top:1299px;left:531px;width:558px;font-size:10.5px;line-height:16.5px;color:#333}
.about-p p+p{margin-top:16px}
/* products */
.products-bg{top:1664px;left:0;width:1200px;height:700px;background:var(--soft)}
.prod-img{position:absolute;top:1788px;width:316px;height:346px;background:#ececec}
.prod-name{position:absolute;top:2152px;font-family:"Arimo",sans-serif;font-size:17px}
.prod-price{position:absolute;top:2183px;font-size:13px}
.prod-more{position:absolute;top:2213px;font-size:11px;color:var(--blue);text-decoration:underline}
/* why */
.why-h{top:2462px;left:112px;font-size:32px}
.why-p{top:2527px;left:112px;width:360px;font-size:10.5px;line-height:16px;color:#333}
.why-li{position:absolute;left:112px;display:flex;align-items:center;gap:14px;font-family:"Arimo",sans-serif;font-size:17px}
/* process */
.step-no{position:absolute;top:14px;right:14px;font-family:"Arimo",sans-serif;font-style:normal;font-size:30px;color:#ececec}
/* gallery */
.gallery-bg{top:3319px;left:0;width:1200px;height:443px;background:var(--soft)}
.gal-h{top:3375px;left:38px;font-size:33px}
.gal-img{position:absolute;top:3439px;height:255px}
/* testimonials */
.quote{top:3912px;left:340px;width:520px;text-align:center;font-size:10.5px;line-height:18px;color:var(--muted)}
/* cta */
.cta-right{top:4099px;left:600px;width:600px;height:466px;background:var(--navy)}
.cta-h{top:4232px;left:709px;color:var(--white);font-size:34px;line-height:40px}
.cta-p{top:4326px;left:709px;width:380px;color:var(--white);font-size:11px;line-height:16px}
/* footer */
.foot-label{position:absolute;top:4646px;font-family:"Arimo",sans-serif;font-size:14px}
.input{position:absolute;top:4683px;left:650px;width:240px;height:34px;border:1px solid #cfcfcf;border-radius:17px;font-size:10px;color:var(--muted);display:flex;align-items:center;padding-left:14px}
.contact{position:absolute;left:957px;display:flex;gap:12px;font-size:12.5px;line-height:17px}
.contact .ic{width:24px;height:24px;border-radius:50%;background:var(--blue);flex:none;display:flex;align-items:center;justify-content:center}
.copy{top:4858px;left:38px;font-size:11px}
</style>
</head>
<body>

<div class="abs topbar">Fresh Purified Water Refills Daily</div>

<div class="photo hero" role="img" aria-label="Owners smiling inside the store in front of stacked refill water bottles"></div>
<div class="abs hero-shade"></div>

<div class="abs brand" style="top:60px;left:36px"><span class="dot"></span><span>Brookvale<br>Fill House</span></div>
<div class="abs nav">
  <span style="left:0">About</span>
  <span style="left:95px">Products</span>
  <span style="left:209px">Water Refills</span>
  <span style="left:345px">Gallery</span>
  <span style="left:443px">Contact</span>
</div>
<svg class="abs" style="top:60px;left:975px" width="18" height="20" viewBox="0 0 18 20" fill="none" stroke="#fff" stroke-width="1.6"><rect x="2" y="6" width="14" height="12" rx="1"/><path d="M6 6V4a3 3 0 0 1 6 0v2"/></svg>
<div class="btn" style="top:52px;left:1025px;width:137px;height:36px">Visit Our Store</div>

<h1 class="abs hero h1" style="position:absolute;top:335px;left:0;width:1200px;height:auto;background:none;text-align:center;color:#fff;font-size:52px;line-height:54px">Elevate Your Hydration.<br>Empower the Planet.</h1>
<div class="abs hero-sub">Premium alkaline water in refillable aluminum bottles —<br>made for active, eco-conscious lifestyles.</div>
<div class="btn" style="top:516px;left:506px;width:188px;height:36px">Refill Water Today</div>

<h2 class="title" style="top:674px">Services Snapshot</h2>

<div class="card" style="top:736px;left:112px;width:234px;height:188px">
  <svg style="top:28px" width="50" height="50" viewBox="0 0 50 50" fill="none" stroke="#1d8fe1" stroke-width="1.8"><circle cx="25" cy="25" r="22"/><path d="M25 12c-6 8-9 13-9 17a9 9 0 0 0 18 0c0-4-3-9-9-17z"/></svg>
  <div class="name" style="top:94px">Water Refills</div>
  <div class="desc" style="top:126px">Affordable, purified,<br>and convenient.</div>
</div>
<div class="card" style="top:736px;left:359px;width:234px;height:188px">
  <svg style="top:28px" width="56" height="50" viewBox="0 0 56 50" fill="none" stroke="#1d8fe1" stroke-width="1.8"><path d="M6 12l12-6 12 6-12 6z"/><path d="M6 12v13l12 6V18"/><path d="M30 12v13l-12 6"/><path d="M26 30l12-6 12 6-12 6z"/><path d="M26 30v12l12 6V36"/><path d="M50 30v12l-12 6"/></svg>
  <div class="name" style="top:94px">Fresh Ice</div>
  <div class="desc" style="top:126px">Perfect for home,<br>parties, and events.</div>
</div>
<div class="card" style="top:736px;left:606px;width:234px;height:188px">
  <svg style="top:28px" width="30" height="50" viewBox="0 0 30 50" fill="none" stroke="#1d8fe1" stroke-width="1.8"><rect x="10" y="2" width="10" height="6"/><path d="M10 8l-4 8v30h18V16l-4-8"/><path d="M6 24h18M6 36h18"/></svg>
  <div class="name" style="top:94px">Hydration Products</div>
  <div class="desc" style="top:126px">Electrolytes, bottles,<br>and accessories.</div>
</div>
<div class="card" style="top:736px;left:853px;width:234px;height:188px">
  <svg style="top:28px" width="50" height="50" viewBox="0 0 50 50" fill="none" stroke="#1d8fe1" stroke-width="1.8"><circle cx="25" cy="18" r="12"/><path d="M17 12h8v6h-6M29 24v-6h5"/><path d="M4 34h10l8 4h10a3 3 0 0 1 0 6H20"/><path d="M32 40l12-6a3 3 0 0 1 3 5L32 48H4"/></svg>
  <div class="name" style="top:94px">Eco-Friendly</div>
  <div class="desc" style="top:126px">Affordable, purified,<br>and convenient.</div>
</div>

<h2 class="abs about-h">Family-Owned.<br>Community-Focused.</h2>
<div class="photo" style="top:1040px;left:723px;width:363px;height:230px;background:linear-gradient(180deg,#2f3f8f 0%,#3a62b0 45%,#1d3278 100%)" role="img" aria-label="Store booth tent at an outdoor community event"></div>
<div class="photo" style="top:1162px;left:112px;width:365px;height:432px;background:linear-gradient(180deg,#cfd6d4 0%,#b9c3c0 40%,#9c907e 75%,#7b6a55 100%)" role="img" aria-label="Owner family standing together on the beach"></div>
<div class="abs about-p">
  <p>At Brookvale Bottleworks, hydration goes far beyond simply quenching thirst; it represents a deep commitment to enhancing both personal health and environmental sustainability. Drawing inspiration from the resilient and vibrant spirit of Brookvale, CO, the brand delivers a premium alkaline water experience thoughtfully designed to meet the needs of today's health-conscious and eco-aware consumers. Their cold-filled, ultra-purified alkaline water is carefully formulated to help neutralize body acidity, support optimal hydration, assist in natural detoxification processes, and promote sustained energy levels throughout the day. Packaged in sturdy, reusable aluminum bottles, it perfectly combines sleek, modern design with a strong focus on sustainability.</p>
  <p>Brookvale Bottleworks is a family-owned business proudly rooted in Brookvale, Colorado. As members of this vibrant community, we're deeply committed to promoting wellness, sustainability, and local partnerships. Every bottle we produce reflects our dedication to health, the environment, and the people we serve — because we don't just do business here, we live here too.</p>
</div>
<div class="btn" style="top:1540px;left:531px;width:186px;height:34px">Learn Our Story</div>

<div class="abs products-bg"></div>
<h2 class="title" style="top:1727px">Featured Products</h2>
<div class="prod-img" style="left:112px;background:linear-gradient(180deg,#efefef,#dfe9f3)" role="img" aria-label="Three blue five-gallon water jugs with splash"></div>
<div class="prod-img" style="left:441px;background:linear-gradient(180deg,#efefef,#e6e6e6)" role="img" aria-label="White aluminum water bottle"></div>
<div class="prod-img" style="left:770px;background:linear-gradient(180deg,#efefef,#dfe9f3)" role="img" aria-label="Three blue five-gallon water jugs with splash"></div>
<div class="prod-name" style="left:112px">Reusable Bottles</div>
<div class="prod-name" style="left:441px">Hydration Accessories</div>
<div class="prod-name" style="left:770px">Dispensers</div>
<div class="prod-price" style="left:112px">$ 120.00</div>
<div class="prod-price" style="left:441px">$ 120.00</div>
<div class="prod-price" style="left:770px">$ 120.00</div>
<div class="prod-more" style="left:112px">Learn More</div>
<div class="prod-more" style="left:441px">Learn More</div>
<div class="prod-more" style="left:770px">Learn More</div>
<div class="btn" style="top:2258px;left:489px;width:220px;height:36px">Shop In-Store</div>

<h2 class="abs why-h">Why Choose Us</h2>
<div class="abs why-p">At Brookvale Fill House, we believe clean water brings people together. We proudly serve our community with affordable hydration solutions and a welcoming local experience.</div>
<div class="why-li" style="top:2605px"><svg width="20" height="20" viewBox="0 0 20 20" fill="none" stroke="#8a8a8a" stroke-width="1.4"><circle cx="10" cy="10" r="8.5"/><path d="M6 10l3 3 6-7"/></svg>Advanced 12-Step Filtration</div>
<div class="why-li" style="top:2658px"><svg width="20" height="20" viewBox="0 0 20 20" fill="none" stroke="#8a8a8a" stroke-width="1.4"><circle cx="10" cy="10" r="8.5"/><path d="M6 10l3 3 6-7"/></svg>Affordable Pricing</div>
<div class="why-li" style="top:2712px"><svg width="20" height="20" viewBox="0 0 20 20" fill="none" stroke="#8a8a8a" stroke-width="1.4"><circle cx="10" cy="10" r="8.5"/><path d="M6 10l3 3 6-7"/></svg>Friendly Family Service</div>
<div class="why-li" style="top:2765px"><svg width="20" height="20" viewBox="0 0 20 20" fill="none" stroke="#8a8a8a" stroke-width="1.4"><circle cx="10" cy="10" r="8.5"/><path d="M6 10l3 3 6-7"/></svg>Sustainable Refill Solutions</div>
<div class="why-li" style="top:2820px"><svg width="20" height="20" viewBox="0 0 20 20" fill="none" stroke="#8a8a8a" stroke-width="1.4"><circle cx="10" cy="10" r="8.5"/><path d="M6 10l3 3 6-7"/></svg>Premium Products Available</div>
<div class="btn" style="top:2874px;left:112px;width:138px;height:34px">Visit Our Store</div>
<div class="photo" style="top:2453px;left:557px;width:529px;height:472px;background:linear-gradient(180deg,#2e5bc0 0%,#2a55b8 55%,#6b6e78 80%,#8a8c92 100%)" role="img" aria-label="Two men shaking hands in the blue-walled store with a surfboard on the wall"></div>

<h2 class="title" style="top:2996px">Our Process</h2>
<div class="card" style="top:3058px;left:112px;width:316px;height:185px;box-shadow:none">
  <span class="step-no">01</span>
  <svg style="top:26px" width="26" height="48" viewBox="0 0 26 48" fill="none" stroke="#1d8fe1" stroke-width="1.8"><rect x="8" y="2" width="10" height="6"/><path d="M8 8l-5 8v30h20V16l-5-8"/><path d="M3 24h20M3 36h20"/></svg>
  <div class="name" style="top:94px">Bring your bottle</div>
  <div class="desc" style="top:126px;font-size:10.5px">Bring your empty bottle or choose from<br>our premium reusable options in-store.</div>
</div>
<div class="card" style="top:3058px;left:441px;width:316px;height:185px;box-shadow:none">
  <span class="step-no">02</span>
  <svg style="top:26px" width="50" height="50" viewBox="0 0 50 50" fill="none" stroke="#1d8fe1" stroke-width="1.8"><circle cx="25" cy="25" r="22"/><path d="M25 12c-6 8-9 13-9 17a9 9 0 0 0 18 0c0-4-3-9-9-17z"/></svg>
  <div class="name" style="top:94px">Refill with Purified Water</div>
  <div class="desc" style="top:126px;font-size:10.5px">Use our advanced 12-step purified water<br>refill station for fresh, clean hydration.</div>
</div>
<div class="card" style="top:3058px;left:770px;width:316px;height:185px;box-shadow:none">
  <span class="step-no">03</span>
  <svg style="top:26px" width="44" height="48" viewBox="0 0 44 48" fill="none" stroke="#1d8fe1" stroke-width="1.8"><circle cx="22" cy="8" r="5"/><path d="M22 13v16M22 18l-12-6M22 18l12-6M22 29l-8 16M22 29l8 16"/></svg>
  <div class="name" style="top:94px">Stay Hydrated</div>
  <div class="desc" style="top:126px;font-size:10.5px">Enjoy cleaner, healthier water while saving<br>money and reducing plastic waste.</div>
</div>

<div class="abs gallery-bg"></div>
<h2 class="abs gal-h">Store Gallery</h2>
<svg class="abs" style="top:3386px;left:1027px" width="58" height="18" viewBox="0 0 58 18" fill="none" stroke="#1c1c1c" stroke-width="1.6"><path d="M20 9H2M8 3L2 9l6 6"/><path d="M38 9h18M50 3l6 6-6 6"/></svg>
<div class="gal-img" style="left:38px;width:264px;background:linear-gradient(180deg,#3a4654,#52606e 50%,#6a7480)" role="img" aria-label="Storefront entrance with open signs in the windows"></div>
<div class="gal-img" style="left:323px;width:265px;background:linear-gradient(90deg,#9aa0a8,#c8ccd2 50%,#2f5cb6)" role="img" aria-label="Filtration tanks and equipment in the back room"></div>
<div class="gal-img" style="left:611px;width:266px;background:linear-gradient(180deg,#8c8478,#a89f92 50%,#c7cbd2)" role="img" aria-label="Owners standing behind rows of bottled water"></div>
<div class="gal-img" style="left:898px;width:264px;background:linear-gradient(180deg,#e6e8ec,#3b63bd 45%,#8a8e96)" role="img" aria-label="Bright store interior with blue walls and refill counter"></div>

<h2 class="title" style="top:3824px">Client Testimonials</h2>
<div class="abs" style="top:3884px;left:0;width:1200px;text-align:center;color:#f0902a;font-size:16px;letter-spacing:4px">★★★★★</div>
<div class="abs quote">Lorem Ipsum has been the industry's standard dummy text ever since the 1500s, when an unknown printer took a galley of type and scrambled it to make a type specimen book. It has survived not only five centuries, but also the leap into electronic typesetting, remaining essentially unchanged. It was popularised in...</div>
<div class="abs" style="top:4004px;left:0;width:1200px;text-align:center;font-size:11px;font-weight:500">Maren Ellis</div>
<div class="abs" style="top:4020px;left:0;width:1200px;text-align:center;font-size:9px;color:var(--muted)">1 month ago</div>
<svg class="abs" style="top:3950px;left:82px" width="24" height="16" viewBox="0 0 24 16" fill="none" stroke="#1c1c1c" stroke-width="1.8"><path d="M22 8H2M8 2L2 8l6 6"/></svg>
<svg class="abs" style="top:3950px;left:1088px" width="24" height="16" viewBox="0 0 24 16" fill="none" stroke="#1c1c1c" stroke-width="1.8"><path d="M2 8h20M16 2l6 6-6 6"/></svg>

<div class="photo" style="top:4099px;left:0;width:600px;height:466px;background:linear-gradient(90deg,#2f5fc2 0%,#3563c0 40%,#8f8f98 70%,#c9c7cc 100%)" role="img" aria-label="Costumed holiday character and a young customer posing in the store"></div>
<div class="abs cta-right"></div>
<h2 class="abs cta-h">Stay Hydrated.<br>Visit Our Store Today.</h2>
<div class="abs cta-p">At Brookvale Fill House, we believe clean water brings people together. We proudly serve our community with affordable hydration solutions and a welcoming local experience.</div>
<div class="btn" style="top:4403px;left:709px;width:185px;height:34px">Get Directions</div>
<div class="btn ghost" style="top:4403px;left:903px;width:183px;height:34px">Contact Us</div>

<div class="abs" style="top:4650px;left:38px;width:178px;height:178px;border-radius:50%;border:9px solid var(--deep);display:flex;align-items:center;justify-content:center;text-align:center;font-family:'Arimo',sans-serif;font-size:17px;line-height:20px;color:var(--mid)">Brookvale<br>Fill House</div>

<div class="foot-label" style="left:498px">Social Links</div>
<div class="abs" style="top:4688px;left:498px;width:36px;height:36px;border-radius:50%;background:var(--blue)" aria-label="Social profile"></div>
<div class="abs" style="top:4688px;left:547px;width:36px;height:36px;border-radius:50%;background:var(--blue)" aria-label="Social profile"></div>

<div class="foot-label" style="left:650px">Subscribe Our Newsletter</div>
<div class="input">Enter your email</div>
<div class="btn" style="top:4730px;left:650px;width:240px;height:34px">Subscribe Now</div>

<div class="foot-label" style="left:957px">Contact Info</div>
<div class="contact" style="top:4680px"><span class="ic"><svg width="12" height="12" viewBox="0 0 12 12" fill="#fff"><path d="M3 1l2 2.5-1.2 1.3a7 7 0 0 0 3.4 3.4L8.5 7 11 9l-1 2C5 11 1 7 1 2z"/></svg></span>(555) 014-2286</div>
<div class="contact" style="top:4718px"><span class="ic"><svg width="12" height="10" viewBox="0 0 12 10" fill="none" stroke="#fff" stroke-width="1.3"><rect x="1" y="1" width="10" height="8"/><path d="M1 1l5 4 5-4"/></svg></span>hello@brookvalefillhouse.com</div>
<div class="contact" style="top:4756px"><span class="ic"><svg width="10" height="13" viewBox="0 0 10 13" fill="#fff"><path d="M5 0a5 5 0 0 1 5 5c0 3-5 8-5 8S0 8 0 5a5 5 0 0 1 5-5z"/><circle cx="5" cy="5" r="1.8" fill="#1d8fe1"/></svg></span><span>4820 W. Alder Creek Rd, Ste. 210<br>Brookvale, CO 80512</span></div>

<div class="abs copy">© Copyright All Right Reserved 2026. brookvalebottleworks.</div>

</body>
</html>
```